Decorative concrete business needs new business cards

Our company attracts homeowners and business with disposable cash. We are a artistic decorative coatings company that will transform your driveway, patio, floors or counter tops into a work of art. We also engrave logos and designs right into the concrete! We are upscale and very professional company. I am open for rearranging our logo on the business card and also to different color patterns. We like the blue and black as in BrushNest's logo. We also like blue and orange/yellow.

Target Market(s)

Adults 30-70

Industry/Entity Type

Concrete

Contact Information for Business Card

Simple: Name, phone, email, website and social media icons

Font styles to use
Serif

Colors

Designer to choose colors to be used in the design.

Requirements
Must have
• Must present a professional upscale appearance. I have attached before and after photos that show you what our industry does. Maybe I will have before and after photo on back of card.
Nice to have
• Artistic, but bold. Nothing whimsical or cute.
Should not have
• Should not have cartoon or childlike appearance.

```html
<!DOCTYPE html>
<html lang="en">
<head>
<meta charset="utf-8">
<title>Crestline Stone Finishes – Business Card</title>
<link rel="stylesheet" href="https://fonts.googleapis.com/css2?family=Marcellus&family=Open+Sans:wght@400;600&display=swap">
<style>
  :root {
    --page: #2a2a2c;
    --card: #1f1f21;
    --card-edge: #2c2c2f;
    --brand-blue: #2b8fca;
    --ink-white: #f4f4f4;
    --ink-soft: #cfcfd2;
    --divider: #2b8fca;
  }
  * { box-sizing: border-box; margin: 0; padding: 0; }
  html, body {
    width: 1200px; height: 1000px; overflow: hidden;
    background: var(--page);
    font-family: "Open Sans", Arial, sans-serif;
  }
  .stage {
    position: relative; width: 1200px; height: 1000px;
  }
  .card {
    position: absolute; left: 250px; width: 700px; height: 400px;
    background: var(--card);
    border: 1px solid var(--card-edge);
    box-shadow: 0 18px 40px rgba(0,0,0,.45);
  }
  .card--back { top: 60px; }
  .card--front { top: 540px; }

  .brand {
    display: flex; align-items: center; gap: 14px;
  }
  .brand__mark {
    width: 22px; height: 22px; background: var(--brand-blue); flex: none;
  }
  .brand__name {
    font-family: "Marcellus", Georgia, serif;
    color: var(--brand-blue);
    font-weight: 400;
    text-transform: uppercase;
    line-height: 1.02;
    border-left: 1px solid var(--divider);
    padding-left: 12px;
  }
  .card--back .brand {
    position: absolute; left: 50%; top: 50%;
    transform: translate(-50%, -50%);
  }
  .card--back .brand__name { font-size: 30px; letter-spacing: 1px; }

  .card--front .brand { position: absolute; left: 48px; top: 42px; }
  .card--front .brand__name { font-size: 32px; letter-spacing: 1px; }

  .person { position: absolute; left: 60px; top: 168px; }
  .person__name {
    color: var(--ink-white); font-weight: 600; font-size: 28px; letter-spacing: .5px;
  }
  .person__role {
    color: var(--brand-blue); font-weight: 600; font-size: 19px; margin-top: 0;
  }

  .contact { position: absolute; left: 44px; top: 262px; list-style: none; }
  .contact__item {
    display: flex; align-items: center; gap: 14px;
    color: var(--ink-soft); font-size: 16px; height: 24px;
  }
  .contact__icon { width: 14px; height: 14px; flex: none; fill: var(--brand-blue); }
  .contact__accent { color: var(--brand-blue); }

  .social {
    position: absolute; left: 36px; top: 340px;
    display: flex; align-items: center; gap: 10px;
    color: var(--ink-soft); font-size: 16px;
  }
  .social__dot { width: 10px; height: 10px; border-radius: 50%; background: var(--brand-blue); }
  .social__handle { color: var(--brand-blue); font-size: 14px; }

  .address {
    position: absolute; left: 30px; top: 368px;
    color: var(--ink-soft); font-size: 16px; letter-spacing: .3px;
  }
</style>
</head>
<body>
<main class="stage">

  <section class="card card--back" aria-label="Business card back">
    <div class="brand">
      <span class="brand__mark"></span>
      <span class="brand__name">Crestline<br>Stone<br>Finishes</span>
    </div>
  </section>

  <section class="card card--front" aria-label="Business card front">
    <div class="brand">
      <span class="brand__mark"></span>
      <span class="brand__name">Crestline<br>Stone<br>Finishes</span>
    </div>

    <div class="person">
      <p class="person__name">ADRIAN VALE</p>
      <p class="person__role">CEO</p>
    </div>

    <ul class="contact">
      <li class="contact__item">
        <svg class="contact__icon" viewBox="0 0 16 16"><path d="M3.5 1.5l2.5 0 1 3.5-1.8 1.2a9 9 0 0 0 4.6 4.6L11 9l3.5 1v2.5c0 1-1 2-2 2C6.5 14.5 1.5 9.5 1.5 3.5c0-1 1-2 2-2z"/></svg>
        <span>+000 123 456 789</span>
      </li>
      <li class="contact__item">
        <svg class="contact__icon" viewBox="0 0 16 16"><path d="M1 3h14v10H1z M2 4l6 5 6-5" fill="none" stroke="#2b8fca" stroke-width="1.4"/></svg>
        <span>yourname@email.com</span>
      </li>
      <li class="contact__item">
        <svg class="contact__icon" viewBox="0 0 16 16"><circle cx="8" cy="8" r="6.5" fill="none" stroke="#2b8fca" stroke-width="1.4"/><path d="M1.5 8h13M8 1.5c-3 3.5-3 9.5 0 13M8 1.5c3 3.5 3 9.5 0 13" fill="none" stroke="#2b8fca" stroke-width="1.2"/></svg>
        <span>www.<span class="contact__accent">crestlinestone</span>.com</span>
      </li>
    </ul>

    <div class="social">
      <span>Follow On</span>
      <span class="social__dot"></span>
      <span class="social__handle">@crestlinestone</span>
    </div>

    <p class="address">Your Street Address, Singapore, 1234</p>
  </section>

</main>
</body>
</html>
```